Digital Menu for New Picnic Company

We're in the process of creating a new picnic business called Fernvale Hampers. We need our menu created as per the content in this google doc https://files.quorvex.net/doc/7Kq2Lm9XpR4tWz8BnC3vYh6JdS5gFa1eTu0iOo/view?share=open
Please look at our website www.fernvalehampers.com.au to get an understanding of what we do and our branding style. We need the menu to be created matching the branding/colours as per our website however other than that please feel free to design it however you like and I will provide feedback from there. We are offering a high end gourmet product so the look and feel of the menu does need to reflect this.
PLEASE NOTE: This menu will only be displayed online as a PDF and doesn't need to be printed or provided physically.

```html
<!DOCTYPE html>
<html lang="en">
<head>
<meta charset="utf-8">
<title>Fernvale Hampers – Gourmet Picnic Menu</title>
<link rel="stylesheet" href="https://fonts.googleapis.com/css2?family=Montserrat:wght@500;600;700&family=Great+Vibes&display=swap">
<style>
:root{
  --mint:#cdeadb;
  --check:#ee7a83;
  --blue:#0aa3e4;
  --green:#62b947;
  --ink:#222;
  --white:#fff;
  --rule:#cfe6cf;
}
*{margin:0;padding:0;box-sizing:border-box}
html,body{width:1200px;height:555px;overflow:hidden;background:var(--mint);font-family:"Montserrat",sans-serif;color:var(--ink)}
.page{position:absolute;top:36px;width:342px;height:482px;background:var(--check);box-shadow:0 1px 3px rgba(0,0,0,.15)}
.page--intro{left:55px}
.page--food{left:429px}
.page--drinks{left:803px}
.sheet{position:absolute;inset:12px;background:var(--white);border-radius:16px}
.frame{position:absolute;inset:17px;border:3px solid var(--blue);border-radius:14px;overflow:hidden}

/* intro page */
.hero{position:absolute;left:0;top:0;width:100%;height:114px;background:linear-gradient(120deg,#2d3a22 0%,#5b4a34 40%,#8a3038 70%,#c88a2e 100%)}
.band{position:absolute;left:0;top:114px;width:100%;height:75px;background:var(--blue)}
.brand{position:absolute;left:50%;top:91px;transform:translateX(-50%);display:flex;align-items:center;gap:5px;background:var(--white);padding:3px 8px;border-radius:10px;font-weight:700;font-size:11px;color:var(--green);white-space:nowrap}
.brand::before{content:"";width:8px;height:8px;border-radius:50%;background:var(--green)}
.intro-title{position:absolute;left:0;width:100%;top:129px;text-align:center;color:var(--white);font-weight:700;font-size:25px;line-height:1}
.intro-sub{position:absolute;left:0;width:100%;top:148px;display:flex;justify-content:center;align-items:center;gap:8px;color:var(--white);font-family:"Great Vibes",cursive;font-size:34px;line-height:1}
.copy{position:absolute;top:206px;width:136px;font-size:6.3px;line-height:10.4px;font-weight:500}
.copy p+p{margin-top:10.4px}
.copy--left{left:18px}
.copy--right{left:164px}
.badge{position:absolute;left:22px;top:364px;width:66px;height:66px;border-radius:50%;background:var(--blue)}

/* shared menu text */
.title{position:absolute;transform:translateX(-50%);color:var(--blue);font-weight:700;white-space:nowrap;line-height:1}
.choose{position:absolute;transform:translateX(-50%);display:flex;align-items:center;gap:6px;font-size:8px;font-weight:500;white-space:nowrap}
.rule{display:block;width:47px;height:3px;background:var(--blue)}
.rule--l{clip-path:polygon(0 45%,85% 0,100% 50%,85% 100%,0 55%)}
.rule--r{clip-path:polygon(0 50%,15% 0,100% 45%,100% 55%,15% 100%)}
.rule--light{background:var(--white);width:50px}
.head{position:absolute;color:var(--green);font-weight:700;font-size:12px;line-height:1}
.list{position:absolute;list-style:none;font-size:7px;line-height:12.6px;font-weight:500;white-space:nowrap}
.list li{position:relative;padding-left:8px}
.list li::before{content:"";position:absolute;left:0;top:4px;width:4px;height:4px;border:1px solid var(--green);border-radius:50%}
.list li.cont::before{display:none}
.divider{position:absolute;left:14px;right:14px;border-top:1px dashed var(--rule)}
.vdivider{position:absolute;border-left:1px dashed var(--rule)}
</style>
</head>
<body>

<section class="page page--intro">
  <div class="sheet"></div>
  <div class="frame">
    <div class="hero" role="img" aria-label="Photo of a picnic setting with champagne glasses, white flowers, an orange and a wicker basket on a red checked cloth"></div>
    <div class="band"></div>
    <div class="brand">Fernvale Hampers</div>
    <h1 class="intro-title">Gourmet Picnic</h1>
    <div class="intro-sub"><span class="rule rule--l rule--light"></span>Menu<span class="rule rule--r rule--light"></span></div>
    <div class="copy copy--left">
      <p>Our Gourmet Picnics are handcrafted and delivered to your picnic spot on a wooden grazing board. The board is sealed inside a catering box to provide peace of mind that your food hasn't been tampered with while waiting for you at the picnic spot.</p>
      <p>Once you arrive, you then open the box and remove the grazing board to begin enjoying the food. We prepare our food in accordance with food handling guidelines and all COVID-19 precautions.</p>
    </div>
    <div class="copy copy--right">
      <p>We also provide complimentary beverages as part of the Gourmet Picnic being your choice of beers, wine or soft drink. You also can choose between still or sparkling water. Beverages are served cold with quality glassware.</p>
      <p>As everyone has varying tastes, we have created our menu to be fully customisable so you can design your own picnic. We offer a wide variety of choices while focussing on quality ingredients for each component of your picnic. This also creates a great excuse to come back for another picnic so you can try out more of the menu.</p>
    </div>
    <div class="badge" role="img" aria-label="Safety certification badge"></div>
  </div>
</section>

<section class="page page--food">
  <div class="sheet"></div>
  <div class="frame">
    <h2 class="title" style="left:154px;top:14px;font-size:21px">Cheese &amp; Dips</h2>
    <div class="choose" style="left:154px;top:37px"><span class="rule rule--l"></span>Choose any 2<span class="rule rule--r"></span></div>
    <h3 class="head" style="left:19px;top:55px">Cheeses</h3>
    <h3 class="head" style="left:109px;top:55px">Dips</h3>
    <ul class="list" style="left:19px;top:71px">
      <li>Creamy Blue</li><li>Blue Vein</li><li>Chilli Cream</li><li>Double Cream Brie</li><li>Camembert</li><li>Cheddar</li><li>Vintage Cheddar</li><li>Parmesan</li><li>Dutch Smoked</li><li>Goat Milk</li>
    </ul>
    <ul class="list" style="left:109px;top:71px">
      <li>Mild Salsa</li><li>Spicy Salsa</li><li>Zesty Avo &amp; Feta</li><li>Roasted Garlic Hommus</li><li>Sweet Potato &amp; Cashew</li><li>Roast Pumpkin,</li><li>Caramelised Onion &amp;</li><li class="cont">Cashews</li><li>Roasted Red Capsicum,</li><li class="cont">Cashews &amp; Basil</li>
    </ul>
    <ul class="list" style="left:216px;top:71px">
      <li>Basil, Pesto &amp;</li><li class="cont">Cashews</li><li>Sweet Chilli &amp; Sour</li><li>Cream</li><li>Caviar</li><li>Guacamole</li><li>Caramalised French</li><li>Onion</li><li>Cheesy Jalapeno</li>
    </ul>
    <div class="divider" style="top:202px"></div>

    <h2 class="title" style="left:154px;top:210px;font-size:21px">Crackers</h2>
    <div class="choose" style="left:154px;top:233px"><span class="rule rule--l"></span>Choose any 2<span class="rule rule--r"></span></div>
    <ul class="list" style="left:19px;top:247px">
      <li>Crispa</li><li>Natural Artisan</li><li>Crackers</li><li>Grainstack</li><li>Flat Bread</li><li>Chilli Jam Flat Bread</li>
    </ul>
    <ul class="list" style="left:113px;top:247px">
      <li>Assorted Crackers</li><li>Veggie Crackers</li><li>Pita Crackers</li><li>Bread Sticks</li><li>Toltos</li><li>Bruschetta Toasts</li>
    </ul>
    <ul class="list" style="left:216px;top:247px">
      <li>Wafer Crackers</li><li>Rice Crackers</li><li>Rye Crispbread</li><li>Gluten Free Crackers</li><li>Seaweed Crackers</li>
    </ul>
    <div class="divider" style="top:328px"></div>
    <div class="vdivider" style="left:129px;top:336px;height:100px"></div>

    <h2 class="title" style="left:66px;top:337px;font-size:19px">Fruits</h2>
    <div class="choose" style="left:66px;top:358px"><span class="rule rule--l" style="width:18px"></span>Choose any 3<span class="rule rule--r" style="width:18px"></span></div>
    <ul class="list" style="left:41px;top:374px">
      <li>Strawberrys</li><li>Grapes</li><li>Passion Fruit</li><li>Oranges</li><li>Kiwi Fruit</li>
    </ul>
    <h2 class="title" style="left:214px;top:337px;font-size:19px">Chocolates</h2>
    <div class="choose" style="left:214px;top:358px"><span class="rule rule--l"></span>Choose any 1<span class="rule rule--r"></span></div>
    <ul class="list" style="left:142px;top:374px">
      <li>Hazel Royale</li><li>Peakbar</li><li>Velour Truffle</li><li>Rocky Road</li><li>Wafo Bar</li>
    </ul>
    <ul class="list" style="left:221px;top:374px">
      <li>Maltbites</li><li>Dairyvale Chocolate</li><li>Vegan/Gluten Free</li><li class="cont">Chocolate or Lolly</li>
    </ul>
  </div>
</section>

<section class="page page--drinks">
  <div class="sheet"></div>
  <div class="frame">
    <h2 class="title" style="left:154px;top:15px;font-size:20px">Complimentary Beverages</h2>
    <div class="choose" style="left:154px;top:39px"><span class="rule rule--l"></span>Choose any 2<span class="rule rule--r"></span></div>
    <h3 class="head" style="left:40px;top:65px">Wine</h3>
    <h3 class="head" style="left:189px;top:65px">Beer</h3>
    <div class="vdivider" style="left:154px;top:61px;height:108px"></div>
    <ul class="list" style="left:40px;top:81px">
      <li>Champagne</li><li>Sauvignon Blanc</li><li>Chadonnay</li><li>Malbec</li><li>Shiraz</li><li>Cabernet Sauvignon</li><li>Merlot</li>
    </ul>
    <ul class="list" style="left:189px;top:81px">
      <li>Craft Lager</li><li>Craft Pale Ale</li><li>Craft XPA</li><li>Australian Lager</li><li>Australian Dry</li><li>International Lager</li><li>Cider</li>
    </ul>
    <div class="divider" style="top:179px"></div>
    <h3 class="head" style="left:40px;top:199px">Water Preference</h3>
    <ul class="list" style="left:40px;top:214px"><li>Still</li></ul>
    <ul class="list" style="left:90px;top:214px"><li>Sparkling</li></ul>
    <ul class="list" style="left:161px;top:214px"><li>Still &amp; Sparkling</li></ul>
    <div class="divider" style="top:238px"></div>
    <h3 class="head" style="left:40px;top:258px">Non Alcoholic</h3>
    <ul class="list" style="left:40px;top:274px">
      <li>Tallowby Cola</li><li>Tallowby No Sugar</li><li>Diet Tallowby</li><li>Tallowby Caffeine Free</li><li>Vanilla Tallowby</li><li>Quillo</li><li>Quillo Max</li><li>Quillo Max Vanilla</li><li>Verdell Lemon Lime</li><li>Orvella</li><li>Ridgemist</li>
    </ul>
    <ul class="list" style="left:161px;top:274px">
      <li>Lemvale</li><li>Lemvale Zero Sugar</li><li>Solbrae</li><li>Solbrae Zero Sugar</li><li>Apple Cider</li><li>Ginger Beer</li><li>Diet Ginger Beer</li><li>Lemon Lime &amp; Bitters</li><li>Creaming Soda</li><li>Sugar Free Creaming</li><li>Soda</li>
    </ul>
  </div>
</section>

</body>
</html>
```